Tradelo Size Charts - 6 Products

Hi Koby,

I had you in mind for this, but we have a new e-commerce store that requires the attached 6 size charts re-designed. They are terrible charts from drop shippers and we need them re-designed to match the Talvoro brand logo to designed.

Chart needs to be white background and black letter's. You can add some smart gradients or design to it if you want to make it look elegant and confident.

Can you design 1 chart and we can amend it to perfection with feedback?
Once we agree on the style - you can then do the same style and design for the remaining charts.

Let me know if this is ok?

```html
<!DOCTYPE html>
<html lang="en">
<head>
<meta charset="utf-8">
<title>Talvoro Size Detail Chart</title>
<link rel="stylesheet" href="https://fonts.googleapis.com/css2?family=Oswald:wght@300;400;500&family=Arimo:wght@400;700&display=swap">
<style>
  :root {
    --page-bg: #ffffff;
    --card-bg: #ffffff;
    --card-edge: #e3e3e3;
    --ink: #111111;
    --ink-soft: #3a3a3a;
    --rule: #111111;
    --title-bg: #111111;
    --title-ink: #ffffff;
    --head-top: #ffffff;
    --head-bottom: #e9e9e9;
    --column-bg: #fafafa;
    --row-1: #f1f1f1;
    --row-2: #ebebeb;
    --row-3: #e4e4e4;
    --row-4: #dddddd;
  }
  * { box-sizing: border-box; margin: 0; padding: 0; }
  html, body { width: 1200px; height: 1200px; overflow: hidden; }
  body {
    background: var(--page-bg);
    position: relative;
    font-family: "Oswald", "Arial Narrow", sans-serif;
    color: var(--ink);
  }
  .chart-card {
    position: absolute;
    left: 39px; top: 228px;
    width: 1122px; height: 744px;
    background: var(--card-bg);
    border: 1px solid var(--card-edge);
    box-shadow: 0 10px 30px rgba(0,0,0,0.08);
  }
  .brand {
    position: absolute;
    left: 0; right: 0; top: 26px;
    display: flex;
    justify-content: center;
    align-items: center;
    gap: 12px;
    font-weight: 500;
    font-size: 26px;
    letter-spacing: 6px;
    color: var(--ink);
  }
  .brand-mark { width: 14px; height: 14px; background: var(--ink); }
  .chart-title {
    position: absolute;
    left: 361px; top: 76px;
    width: 400px; height: 58px;
    background: var(--title-bg);
    color: var(--title-ink);
    font-weight: 400;
    font-size: 30px;
    line-height: 58px;
    text-align: center;
    letter-spacing: 1px;
  }
  .chart-notes {
    position: absolute;
    left: 70px; top: 160px;
    width: 982px;
    list-style: none;
    color: var(--ink-soft);
    font-weight: 300;
    font-size: 22px;
    line-height: 31px;
  }
  .chart-notes li { padding-left: 28px; text-indent: -28px; }
  .chart-column {
    position: absolute;
    top: 300px;
    width: 260px; height: 384px;
    background: var(--column-bg);
    border: 1px solid var(--card-edge);
    border-top: 4px solid var(--rule);
    box-shadow: 0 4px 14px rgba(0,0,0,0.07);
  }
  .column-size { left: 151px; }
  .column-bust { left: 431px; }
  .column-length { left: 711px; }
  .column-header {
    height: 66px;
    background: linear-gradient(180deg, var(--head-top), var(--head-bottom));
    border-bottom: 1px solid var(--card-edge);
    font-weight: 500;
    font-size: 34px;
    line-height: 66px;
    letter-spacing: 3px;
    text-align: center;
    color: var(--ink);
  }
  .column-rows {
    list-style: none;
    margin-top: 40px;
    display: flex;
    flex-direction: column;
    gap: 8px;
  }
  .column-rows li {
    height: 50px;
    display: flex;
    align-items: center;
    justify-content: center;
    font-family: "Arimo", Arial, sans-serif;
    font-size: 20px;
    color: var(--ink);
  }
  .column-rows li:nth-child(1) { background: var(--row-1); }
  .column-rows li:nth-child(2) { background: var(--row-2); }
  .column-rows li:nth-child(3) { background: var(--row-3); }
  .column-rows li:nth-child(4) { background: var(--row-4); }
  .column-size li { justify-content: flex-start; padding-left: 30px; gap: 16px; }
  .tick-icon { width: 30px; height: 30px; flex: none; }
</style>
</head>
<body>
  <div class="chart-card">
    <div class="brand"><span class="brand-mark"></span>TALVORO</div>
    <h1 class="chart-title">SIZE DETAIL (1″ = 2.54 CM)</h1>
    <ol class="chart-notes">
      <li>1.&nbsp; To make sure you get the right size, please refer to our size chart before buying. If you are not sure about your size, please email us your exact body measurements and we will suggest the right size. Thank you for your understanding.</li>
      <li>2.&nbsp; Manual measurements may differ by 1–3 cm.</li>
    </ol>

    <section class="chart-column column-size">
      <h2 class="column-header">SIZE</h2>
      <ul class="column-rows">
        <li><svg class="tick-icon" viewBox="0 0 30 30" aria-hidden="true"><circle cx="15" cy="15" r="13" fill="none" stroke="#111" stroke-width="2"/><path d="M9.5 15.5l3.8 3.8 7.2-7.6" fill="none" stroke="#111" stroke-width="2.5" stroke-linecap="round" stroke-linejoin="round"/></svg>Asian Size: S</li>
        <li><svg class="tick-icon" viewBox="0 0 30 30" aria-hidden="true"><circle cx="15" cy="15" r="13" fill="none" stroke="#111" stroke-width="2"/><path d="M9.5 15.5l3.8 3.8 7.2-7.6" fill="none" stroke="#111" stroke-width="2.5" stroke-linecap="round" stroke-linejoin="round"/></svg>Asian Size: M</li>
        <li><svg class="tick-icon" viewBox="0 0 30 30" aria-hidden="true"><circle cx="15" cy="15" r="13" fill="none" stroke="#111" stroke-width="2"/><path d="M9.5 15.5l3.8 3.8 7.2-7.6" fill="none" stroke="#111" stroke-width="2.5" stroke-linecap="round" stroke-linejoin="round"/></svg>Asian Size: L</li>
        <li><svg class="tick-icon" viewBox="0 0 30 30" aria-hidden="true"><circle cx="15" cy="15" r="13" fill="none" stroke="#111" stroke-width="2"/><path d="M9.5 15.5l3.8 3.8 7.2-7.6" fill="none" stroke="#111" stroke-width="2.5" stroke-linecap="round" stroke-linejoin="round"/></svg>Asian Size: XL</li>
      </ul>
    </section>

    <section class="chart-column column-bust">
      <h2 class="column-header">BUST</h2>
      <ul class="column-rows">
        <li>Bust: 80 cm / 31.5″</li>
        <li>Bust: 84 cm / 33.1″</li>
        <li>Bust: 88 cm / 34.6″</li>
        <li>Bust: 92 cm / 36.2″</li>
      </ul>
    </section>

    <section class="chart-column column-length">
      <h2 class="column-header">LENGTH</h2>
      <ul class="column-rows">
        <li>Length: 80 cm / 31.5″</li>
        <li>Length: 82 cm / 32.2″</li>
        <li>Length: 84 cm / 33.1″</li>
        <li>Length: 86 cm / 33.8″</li>
      </ul>
    </section>
  </div>
</body>
</html>
```